" Eu ( geriatra) vou ampliar meu Consultorio para uma empresa especializada no atendimento integral, personalizado e multiprofissional ao idoso. A ideia é oferecer pacotes com maior ou menor grau de atendimentos multiprofissionais "

```html
<!DOCTYPE html>
<html lang="pt-BR">
<head>
<meta charset="utf-8">
<title>Velina Saúde Geriátrica – Capa e Perfil</title>
<link rel="stylesheet" href="https://fonts.googleapis.com/css2?family=Montserrat:wght@300;400;500&display=swap">
<style>
  :root {
    --page-bg: #eceef2;
    --cover-top: #ffffff;
    --cover-mist: #e6ebf0;
    --ink-grey: #8c8c8c;
    --ink-dark: #6f6f6f;
    --gold-light: #efe3cc;
    --gold-mid: #e0cca6;
    --gold-line: #b59a6a;
    --brown: #8a6e47;
    --icon-bg: #8c8c8c;
  }
  * { margin: 0; padding: 0; box-sizing: border-box; }
  html, body {
    width: 1200px; height: 1200px; overflow: hidden;
    background: var(--page-bg);
    font-family: "Montserrat", sans-serif;
  }
  .cover {
    position: absolute; left: 50px; top: 140px;
    width: 1100px; height: 456px;
    overflow: hidden;
    background: linear-gradient(100deg, var(--cover-mist) 0%, var(--cover-top) 45%, var(--cover-top) 100%);
    box-shadow: 0 2px 10px rgba(0,0,0,.08);
  }
  .cover__photo {
    position: absolute; left: 0; top: 0; width: 520px; height: 456px;
    background: radial-gradient(ellipse at 30% 40%, #d5dde5 0%, rgba(230,235,240,.6) 45%, rgba(255,255,255,0) 75%);
  }
  .cover__wave { position: absolute; left: 0; bottom: 0; width: 1100px; height: 110px; }
  .brand-mark {
    position: absolute; left: 180px; top: 165px;
    width: 150px; height: 150px; border-radius: 50%;
    background: var(--gold-mid);
  }
  .brand-name {
    position: absolute; left: 640px; top: 40px;
    font-weight: 300; font-size: 128px; line-height: 1;
    color: var(--ink-grey); letter-spacing: 2px;
  }
  .brand-tagline {
    position: absolute; left: 650px; top: 172px;
    font-weight: 400; font-size: 24px; color: var(--ink-grey); letter-spacing: 1px;
  }
  .contact {
    position: absolute; right: 28px; top: 212px;
    text-align: right; color: var(--ink-dark);
  }
  .contact__row {
    display: flex; justify-content: flex-end; align-items: center; gap: 12px;
    font-size: 25px; height: 36px;
  }
  .contact__icon {
    width: 26px; height: 26px; border-radius: 4px; background: var(--icon-bg);
    display: flex; align-items: center; justify-content: center;
  }
  .contact__address { font-size: 20px; line-height: 28px; margin-top: 6px; }
  .profile {
    position: absolute; left: 50px; top: 650px;
    width: 400px; height: 400px; overflow: hidden;
    background: linear-gradient(135deg, #dfe6ec 0%, #ffffff 55%, #f4f6f8 100%);
    box-shadow: 0 2px 10px rgba(0,0,0,.08);
  }
  .profile__mark {
    position: absolute; left: 250px; top: 40px;
    width: 80px; height: 80px; border-radius: 50%; background: var(--gold-mid);
  }
  .profile__name {
    position: absolute; left: 0; right: 0; top: 170px; text-align: center;
    font-weight: 300; font-size: 92px; line-height: 1; color: var(--ink-grey);
  }
  .profile__tagline {
    position: absolute; left: 0; right: 0; top: 272px; text-align: center;
    font-size: 20px; color: var(--ink-grey); letter-spacing: 1px;
  }
</style>
</head>
<body>
  <section class="cover">
    <div class="cover__photo" role="img" aria-label="Foto suave e desfocada de ambiente de cuidado ao idoso"></div>
    <div class="brand-mark"></div>
    <div class="brand-name">Velina</div>
    <div class="brand-tagline">Saúde Geriátrica</div>

    <div class="contact">
      <div class="contact__row">
        <span>(00)&nbsp; 0000 0000 | 0000 0000</span>
        <span class="contact__icon">
          <svg width="16" height="16" viewBox="0 0 24 24"><path fill="#fff" d="M6.6 10.8a15 15 0 0 0 6.6 6.6l2.2-2.2a1 1 0 0 1 1-.25 11.4 11.4 0 0 0 3.6.57 1 1 0 0 1 1 1V20a1 1 0 0 1-1 1A17 17 0 0 1 3 4a1 1 0 0 1 1-1h3.5a1 1 0 0 1 1 1c0 1.25.2 2.45.57 3.57a1 1 0 0 1-.25 1z"/></svg>
        </span>
      </div>
      <div class="contact__row">
        <span>(00)&nbsp; +55 0000 0000</span>
        <span class="contact__icon"></span>
      </div>
      <div class="contact__row contact__address">
        <span>Avenida das Acácias, 850,</span>
        <span class="contact__icon">
          <svg width="16" height="16" viewBox="0 0 24 24"><path fill="#fff" d="M12 2a7 7 0 0 0-7 7c0 5.2 7 13 7 13s7-7.8 7-13a7 7 0 0 0-7-7zm0 9.5A2.5 2.5 0 1 1 12 6.5a2.5 2.5 0 0 1 0 5z"/></svg>
        </span>
      </div>
      <div class="contact__address" style="margin-right:38px">Sala 210-212 | Centro - Vila Serena | RJ</div>
    </div>

    <svg class="cover__wave" viewBox="0 0 1100 110" preserveAspectRatio="none">
      <path d="M0 40 C 300 90, 700 10, 1100 30 L1100 110 L0 110 Z" fill="var(--gold-light)"/>
      <path d="M0 60 C 320 105, 720 35, 1100 55 L1100 110 L0 110 Z" fill="var(--gold-mid)"/>
      <path d="M0 40 C 300 90, 700 10, 1100 30" fill="none" stroke="var(--brown)" stroke-width="3"/>
      <path d="M0 60 C 320 105, 720 35, 1100 55" fill="none" stroke="var(--gold-line)" stroke-width="1.5"/>
    </svg>
  </section>

  <section class="profile">
    <div class="profile__mark"></div>
    <div class="profile__name">Velina</div>
    <div class="profile__tagline">Saúde Geriátrica</div>
  </section>
</body>
</html>
```